Dr Maren Holt, Orthopaedic Hand Surgeon

I am an orthopaedic hand surgeon and need business cards that reflect the surgery I do. I operate on bones, ligaments, tendons, and soft tissues. I can do microsurgery (surgery under an operating microscope) - including connecting ends of cut nerves and arteries in the fingers together. As an orthopaedic surgeon, I also fix fractures and manage orthopaedic trauma in the rest of the body. I favour black as a colour, and have some pictures of hand X-rays that you can use in the design, if you think that would look good (feel free to crop).

Hi all. Thank you for all your submissions so far. Please note that I have updated my project brief. I would like to emphasise that use of the logos that I have provided is optional, and if used, I would very much prefer the logo not to dominate the card, but add to the overall aesthetic of the card. Warm regards, Maren

Target Market(s)

Referring medical practitioners, hand therapists, patients

Industry/Entity Type

Healthcare

Contact Information for Business Card

Dr Maren Holt
Orthopaedic Hand Surgeon
MBBS BSc (Med), MIntPH (Merit), GWELN (Ortho), MIvroE

Font styles to use
Serif

Colors

Designer to choose colors to be used in the design.

Requirements
Must have
• Space for:
• 2 addresses (a PO Box Address and a consulting suite address) - to be confirmed
• 1 phone number - to be confirmed
Nice to have
• Please choose one of the GWELN logos (I included 3 - colour, black reverse, and greyscale); if you include this in the design, IT SHOULD NOT DOMINATE THE CARD, but be smaller and more discreet.
• I have also attached the MIvroE logo (colour and greyscale); if you choose to include this in the design, IT SHOULD NOT DOMINATE THE CARD, but be smaller and more discreet.
• I would love to be able to update details on the card as time goes on, and thus would like to own the template for the card as well.
• Also I would love discussion with regard to any changes on the card, if I am not completely happy with the design, and would like to discuss things such as ease of printing, finish on the cards (matte, polish) etc.
Should not have
• I don't like the card to look too crowded

```html
<!DOCTYPE html>
<html lang="en">
<head>
<meta charset="utf-8">
<title>Dr Maren Holt – Business Card</title>
<link rel="stylesheet" href="https://fonts.googleapis.com/css2?family=Nunito+Sans:wght@300;400&display=swap">
<style>
  :root {
    --page-bg: #ececec;
    --panel-light-top: #dcdcde;
    --panel-light-bottom: #c9cacc;
    --panel-dark-top: #5b5c5f;
    --panel-dark-bottom: #8a8b8e;
    --accent-blue: #80b3e0;
    --ink-white: #f4f4f4;
    --ink-soft: #e2e2e2;
    --logo-ink: #5f7f97;
    --logo-mark: #b9a07a;
    --caption-ink: #6d6e70;
  }
  html, body {
    margin: 0;
    width: 1200px;
    height: 720px;
    overflow: hidden;
    background: var(--page-bg);
  }
  .canvas {
    position: relative;
    width: 1200px;
    height: 720px;
  }
  .business-card {
    position: absolute;
    left: 100px;
    top: 60px;
    width: 1000px;
    height: 600px;
    overflow: hidden;
    box-shadow: 0 6px 24px rgba(0,0,0,0.12);
    font-family: "Nunito Sans", sans-serif;
  }
  .card-background {
    position: absolute;
    inset: 0;
    display: block;
  }
  .college-mark {
    position: absolute;
    left: 640px;
    top: 46px;
    display: flex;
    align-items: center;
    gap: 14px;
  }
  .college-mark__dot {
    width: 46px;
    height: 46px;
    border-radius: 50%;
    background: var(--logo-mark);
  }
  .college-mark__name {
    font-size: 46px;
    font-weight: 300;
    color: var(--logo-ink);
    letter-spacing: 1px;
  }
  .college-mark__caption {
    font-size: 15px;
    font-weight: 400;
    color: var(--caption-ink);
    line-height: 1.25;
    margin-left: 4px;
  }
  .identity {
    position: absolute;
    left: 64px;
    top: 392px;
    color: var(--ink-white);
  }
  .identity__name {
    margin: 0;
    font-size: 66px;
    font-weight: 400;
    letter-spacing: 2px;
    line-height: 1;
  }
  .identity__role {
    margin: 12px 0 0 58px;
    font-size: 30px;
    font-weight: 300;
    letter-spacing: 1px;
    color: var(--ink-soft);
  }
  .identity__credentials {
    margin: 8px 0 0 58px;
    font-size: 21px;
    font-weight: 300;
    color: var(--ink-soft);
  }
</style>
</head>
<body>
<div class="canvas">
  <div class="business-card">
    <svg class="card-background" width="1000" height="600" viewBox="0 0 1000 600" aria-hidden="true">
      <defs>
        <linearGradient id="panelLight" x1="0" y1="0" x2="0" y2="1">
          <stop offset="0" stop-color="var(--panel-light-top)"/>
          <stop offset="1" stop-color="var(--panel-light-bottom)"/>
        </linearGradient>
        <linearGradient id="panelDark" x1="0" y1="0" x2="0.3" y2="1">
          <stop offset="0" stop-color="var(--panel-dark-top)"/>
          <stop offset="1" stop-color="var(--panel-dark-bottom)"/>
        </linearGradient>
      </defs>
      <rect width="1000" height="600" fill="url(#panelLight)"/>
      <polygon points="0,0 380,0 1000,430 1000,600 0,600" fill="url(#panelDark)"/>
      <line x1="380" y1="0" x2="1000" y2="430" stroke="var(--accent-blue)" stroke-width="11"/>
    </svg>

    <div class="college-mark">
      <span class="college-mark__dot"></span>
      <span class="college-mark__name">GWELN</span>
      <span class="college-mark__caption">Fellow of the<br>Meridian College of Surgeons</span>
    </div>

    <div class="identity">
      <h1 class="identity__name">DR. MAREN HOLT</h1>
      <p class="identity__role">ORTHOPAEDIC HAND SURGEON</p>
      <p class="identity__credentials">MBBS BSc (Med), MIntPH (Merit), GWELN (Ortho), MIvroE</p>
    </div>
  </div>
</div>
</body>
</html>
```